Sales Flyer offering home being built and items included as well as options

We are custom home builders and we need a flyer to place in literature boxes on lots where we are building a house. Most times it's a lot and home package. But sometimes it's just a home to be built on someone lot they already own. We'd like it to list items that are included and the options being offered. It will have to have our business contact info., website info, etc.
We'd like it to have colors to go with our website and logo.
www.fendrickandloame.com. You may use some of the wording from our website if needed. We want a place to upload the house that we intend to build, which will change, (not all projects are the same house) plus maybe side stock pictures of our homes or things inside the home we have built.
This file would have to be so that it will allow us to change the sales price, items included and options from time to time and anything else that needs to changed, depending upon where we are building. I will upload an example of one we have used in the past that I did myself. But I know it can be done better

Target Market(s)

People looking for new custom home to be constructed. Usually people driving by.

Industry/Entity Type

Building

Colors

Designer to choose colors to be used in the design.

Requirements
Must have
• This is a sales flyer. Need to be professional and eye catchy, but yet elegant, pleasing to the eye.
• Our company information (see website) or current flyer uploaded.
• Website info.
• Logo (see website)
• Facebook info
• Need to be able to make changes to flyer. Can not be in just PDF
• Need to be able to print in our office, since each project changes.
• Picture of house being built, picture on flyer uploaded is the current home being offered. Must have items included and options being offered
Nice to have
• Stock pictures. Colors to go with website and logo.

```html
<!DOCTYPE html>
<html lang="en">
<head>
<meta charset="utf-8">
<title>Fendrick and Loame – Lot and Home Package Flyer</title>
<link href="https://fonts.googleapis.com/css2?family=Marcellus&family=Source+Sans+3:wght@400;600;700&display=swap" rel="stylesheet">
<style>
  :root{
    --canvas:#e9e6e1;
    --charcoal:#242424;
    --charcoal-2:#2f2f2f;
    --paper:#f2f2f2;
    --gold:#b8913a;
    --gold-light:#d8b765;
    --ink:#1e1e1e;
    --grey-text:#555555;
    --option-bg:#e3e3e3;
    --white:#ffffff;
  }
  *{box-sizing:border-box;margin:0;padding:0}
  html,body{width:1005px;height:1200px;overflow:hidden;background:var(--canvas)}
  .flyer{
    position:absolute;left:39px;top:0;width:850px;height:1100px;
    transform:scale(1.0909);transform-origin:0 0;
    background:var(--paper);font-family:"Source Sans 3",Arial,sans-serif;color:var(--ink);
    overflow:hidden;
  }
  .flyer__top{
    position:absolute;left:0;top:0;width:850px;height:610px;
    background:linear-gradient(180deg,var(--charcoal-2),var(--charcoal));
  }
  .brand{position:absolute;left:62px;top:44px;display:flex;align-items:center;gap:14px}
  .brand__mark{width:40px;height:40px;background:var(--gold)}
  .brand__name{font-family:"Marcellus",Georgia,serif;font-size:27px;letter-spacing:1px;color:var(--gold-light);line-height:1}
  .headline{position:absolute;right:40px;top:24px;text-align:right}
  .headline__title{font-size:54px;font-weight:400;color:var(--white);line-height:1;letter-spacing:.5px}
  .headline__sub{margin-top:12px;font-size:20px;font-weight:400;color:var(--gold-light);letter-spacing:.2px}
  .hero{
    position:absolute;left:43px;top:148px;width:767px;height:353px;
    background:linear-gradient(180deg,#a9b1bb 0%,#cfd3d8 28%,#c7b08f 40%,#9a5534 58%,#6c6a60 74%,#5f8a3c 82%,#4d7a30 100%);
  }
  .badge{position:absolute;left:685px;top:359px;width:140px;height:140px}
  .badge svg{position:absolute;inset:0}
  .badge__text{position:absolute;inset:0;display:flex;align-items:center;justify-content:center;text-align:center;
    color:var(--white);font-size:20px;font-weight:600;line-height:25px}
  .gallery{position:absolute;left:40px;top:524px;width:770px;height:178px;background:var(--white);display:flex;gap:6px;padding:5px}
  .gallery__photo{flex:1}
  .gallery__photo--framing{background:linear-gradient(160deg,#3f6fb5 0%,#8fb2de 50%,#c9a882 75%,#8c6f52 100%)}
  .gallery__photo--kitchen{background:linear-gradient(180deg,#e9e4dc 0%,#d9d2c6 45%,#8a4a26 75%,#6a3415 100%)}
  .gallery__photo--bath{background:linear-gradient(160deg,#f1eee8 0%,#d8cbb4 50%,#b89f7c 80%,#6b5a46 100%)}
  .features{position:absolute;top:730px;list-style:none;font-size:14.5px;line-height:19.4px;color:var(--ink)}
  .features li::before{content:"• "}
  .features--left{left:43px}
  .features--right{left:318px}
  .options{position:absolute;left:535px;top:730px;width:260px}
  .options__header{height:28px;background:#111;color:var(--gold-light);font-size:14.5px;font-weight:600;letter-spacing:.8px;padding:5px 0 0 15px;
    clip-path:polygon(0 0,100% 0,100% 100%,3% 100%)}
  .options__body{margin-left:3px;height:125px;background:var(--option-bg);padding:6px 0 0 8px}
  .options__list{list-style:none;display:grid;grid-template-columns:130px 120px;row-gap:5.6px;font-size:10.5px;color:var(--ink);text-transform:uppercase}
  .options__list li{position:relative;padding-left:12px;line-height:14px}
  .options__list li::before{content:"";position:absolute;left:1px;top:3px;width:6px;height:3px;border-left:1.4px solid var(--ink);border-bottom:1.4px solid var(--ink);transform:rotate(-45deg)}
  .options__price{margin-top:13px;text-align:center;font-family:"Marcellus",Georgia,serif;font-size:14.5px;letter-spacing:1px;color:var(--gold)}
  .promise{position:absolute;left:0;top:914px;width:850px;height:62px;background:var(--gold);
    display:flex;align-items:center;justify-content:center;font-family:"Marcellus",Georgia,serif;font-size:31px;letter-spacing:1.2px;color:var(--white)}
  .contact{position:absolute;left:0;top:993px;width:850px;text-align:center}
  .contact__motto{font-size:17px;font-weight:600;color:var(--ink);letter-spacing:.3px}
  .contact__address{margin-top:10px;font-size:19px;color:var(--grey-text);letter-spacing:.3px}
  .contact__call{margin-top:8px;font-size:18.5px;color:var(--gold);letter-spacing:.3px}
</style>
</head>
<body>
<main class="flyer">
  <section class="flyer__top">
    <div class="brand">
      <span class="brand__mark"></span>
      <span class="brand__name">FENDRICK AND LOAME</span>
    </div>
    <header class="headline">
      <h1 class="headline__title">INCLUDED!</h1>
      <p class="headline__sub">IN THIS LOT AND HOME PACKAGE</p>
    </header>
    <div class="hero" role="img" aria-label="Photo of the featured home: tan and red-sided house with porch, garage and front lawn"></div>
    <div class="badge">
      <svg viewBox="0 0 140 140" width="140" height="140" aria-hidden="true">
        <polygon fill="#b8913a" points="140,70 127.96,85.54 130.62,105 112.42,112.42 105,130.62 85.54,127.96 70,140 54.46,127.96 35,130.62 27.58,112.42 9.38,105 12.04,85.54 0,70 12.04,54.46 9.38,35 27.58,27.58 35,9.38 54.46,12.04 70,0 85.54,12.04 105,9.38 112.42,27.58 130.62,35 127.96,54.46"/>
      </svg>
      <div class="badge__text">YOUR<br>DESIGN OR<br>OURS!</div>
    </div>
    <div class="gallery">
      <div class="gallery__photo gallery__photo--framing" role="img" aria-label="Photo of house framing under construction"></div>
      <div class="gallery__photo gallery__photo--kitchen" role="img" aria-label="Photo of kitchen with white cabinets, island and hardwood floor"></div>
      <div class="gallery__photo gallery__photo--bath" role="img" aria-label="Photo of bathroom with granite vanity and glass tile shower"></div>
    </div>
  </section>

  <ul class="features features--left">
    <li>3 Bedroom</li>
    <li>2 Full Baths</li>
    <li>Custom Tile Shower w/glass enclosure</li>
    <li>Gourment Kitchen</li>
    <li>Granite Counter Top</li>
    <li>Stainless Steel Appliances</li>
    <li>Hardwood and tile floors</li>
    <li>Carpet in Bedrooms</li>
  </ul>
  <ul class="features features--right">
    <li>9’ Ceilings</li>
    <li>36” Propane Fireplace</li>
    <li>Custom Trim Pkg.</li>
    <li>Crown molding included</li>
    <li>Custom Painting</li>
    <li>Septic &amp; Well</li>
    <li>Asphalt driveway</li>
    <li>Corvane Tankless Water Heather</li>
  </ul>

  <aside class="options">
    <h2 class="options__header">OPTION AVAILABLE</h2>
    <div class="options__body">
      <ul class="options__list">
        <li>Soaker Tub</li>
        <li>Screen Porch</li>
        <li>4 Season Sunroom</li>
        <li>Outdoor Shower</li>
        <li>Landscape Pkg</li>
        <li>Bonus Room</li>
        <li>Irrigation System</li>
        <li>Deck</li>
      </ul>
      <p class="options__price">SALE PRICE $ 289,900</p>
    </div>
  </aside>

  <div class="promise">We will design and build your Dream home!</div>

  <footer class="contact">
    <p class="contact__motto">BUILDING HOMES - BUILDING RELATIONSHIPS</p>
    <p class="contact__address">1180 MARSH HOLLOW RD |&nbsp; MILLBROOK, DE 19960 |&nbsp; WWW.FENDRICKANDLOAME.COM</p>
    <p class="contact__call">CALL US ANYTIME 302.555.0148</p>
  </footer>
</main>
</body>
</html>
```